Business Card Design for Kidvale (Hires out childrens play areas)

Looking to have a business card designed for a company we just bought. The company rents out childrens play areas.

I have uploaded a couple of examples of the kind of business card style I like. Here are two more examples:

https://quorvastudio.nz/project/bright-romp-branding/
https://imgvaultcdn.com/design_img/8841052/302917/302917_5518203_8841052_b73e19a2_image.jpg

I think a white card will be best due to all the colours in the logo.

Size we require: 3.75" x 2.25" (horizontally orientated) with a 0.125" bleed

Uploaded is two versions of our logo.

Details for the card:
1. My name: Liam Verster
2. Title: Managing Director
3. Phone no: 021 563 417
4. Email: liam@kidvale.co.nz
5. URL: www.kidvale.co.nz
6. Address:
PO Box 318625
Fernlea, Auckland

Let me know if you need anything else.

Target Market(s)

Hospitals, doctors surgeries, bed shops, etc.

Contact Information for Business Card

Details for the card:
1. My name: Liam Verster
3. Phone no: 021 563 417
5. URL: www.kidvale.co.nz
6. Address:
PO Box 318625
Fernlea, Auckland

Requirements
Should not have
• Not too busy.

```html
<!DOCTYPE html>
<html lang="en">
<head>
<meta charset="utf-8">
<title>Kidvale Business Card</title>
<link href="https://fonts.googleapis.com/css2?family=Questrial&family=Quicksand:wght@700&display=swap" rel="stylesheet">
<style>
  :root {
    --bg: #2b2d31;
    --card: #ffffff;
    --blue: #1462b8;
    --orange: #f7931e;
    --teal: #1b9ba1;
    --red: #e2231a;
    --green: #39a935;
    --purple: #9a3db8;
    --magenta: #d62ea8;
    --ink: #3a3a3a;
  }
  * { box-sizing: border-box; margin: 0; padding: 0; }
  html, body {
    width: 1200px; height: 900px; overflow: hidden;
    background: var(--bg);
    font-family: "Questrial", "Century Gothic", sans-serif;
  }
  .canvas {
    width: 1200px; height: 900px;
    display: flex; flex-direction: column;
    align-items: center; justify-content: center; gap: 60px;
  }
  .card {
    position: relative;
    width: 560px; height: 336px;
    background: var(--card);
    overflow: hidden;
    box-shadow: 0 10px 30px rgba(0,0,0,.45);
  }

  /* Front */
  .card-front { display: flex; align-items: center; justify-content: center; gap: 18px; }
  .brand-mark { width: 34px; height: 34px; background: var(--orange); }
  .brand-name {
    font-family: "Quicksand", sans-serif; font-weight: 700;
    font-size: 64px; color: var(--blue); letter-spacing: 1px;
  }

  /* Back */
  .name-band {
    position: absolute; left: 40px; right: 0; top: 38px; height: 78px;
    background: var(--blue);
    padding: 8px 0 0 26px;
  }
  .person-name { font-size: 34px; line-height: 38px; color: var(--orange); }
  .person-title { font-size: 17px; color: #fff; margin-top: 2px; }
  .mascot {
    position: absolute; left: 350px; top: 74px;
    width: 180px; height: 180px; border-radius: 50%;
    border: 10px solid var(--card);
    background: radial-gradient(circle at 40% 35%, var(--magenta), var(--purple));
  }
  .contact {
    position: absolute; left: 40px; top: 146px;
    list-style: none; font-size: 15px; line-height: 24px; color: var(--ink);
  }
  .address {
    position: absolute; right: 44px; top: 252px;
    font-size: 17px; line-height: 22px; color: var(--ink); text-align: right; font-style: normal;
  }
  .color-strip { position: absolute; left: 0; right: 0; bottom: 0; height: 20px; display: flex; }
  .color-strip span { flex: 1; }
  .strip-teal { background: var(--teal); }
  .strip-red { background: var(--red); }
  .strip-green { background: var(--green); }
  .strip-orange { background: var(--orange); }
</style>
</head>
<body>
<main class="canvas">
  <section class="card card-front">
    <span class="brand-mark"></span>
    <span class="brand-name">Kidvale</span>
  </section>

  <section class="card card-back">
    <div class="name-band">
      <div class="person-name">Liam Verster</div>
      <div class="person-title">Managing Director</div>
    </div>
    <div class="mascot" role="img" aria-label="Kidvale mascot illustration area"></div>
    <ul class="contact">
      <li>021 563 417</li>
      <li>liam@kidvale.co.nz</li>
      <li>www.kidvale.co.nz</li>
    </ul>
    <address class="address">PO Box 318625<br>Fernlea, Auckland</address>
    <div class="color-strip">
      <span class="strip-teal"></span>
      <span class="strip-red"></span>
      <span class="strip-green"></span>
      <span class="strip-orange"></span>
    </div>
  </section>
</main>
</body>
</html>
```